Fahrzeugbeschriftung für Zahnarztpraxis
Zielgruppe
Zahnarztpraxis. Das jetzige Logo ist bereits von grafikmarkt
Aufgabenstellung
Bestandslogo und dieses Grün verwenden . ( ist von Euch ) . Damals wurde ein Wettbewerb von der Zahnarztpraxis ausgeschrieben . Adresse und Kontaktdaten sollten hervorgehoben werde.
Lustig mit Wiedererkennungseffekt ( Zahnfee muss nicht sein ) die zukünftigen Folien sollten auf die Flächen und die veloran stimmig passen

```html
<!DOCTYPE html>
<html lang="de">
<head>
<meta charset="utf-8">
<title>Fahrzeugbeschriftung KLARBISS Zahnärzte</title>
<link href="https://fonts.googleapis.com/css2?family=Lato:wght@400;700&display=swap" rel="stylesheet">
<style>
  :root {
    --bg: #e9eaea;
    --panel: #ffffff;
    --panel-edge: #d4d6d6;
    --green: #9cc31d;
    --grey: #6e6f70;
    --grey-dark: #555657;
    --fairy-tone: linear-gradient(160deg, #c9dd7a 0%, #eef2e4 55%, #ffffff 100%);
  }
  html, body {
    margin: 0;
    width: 1200px;
    height: 1006px;
    overflow: hidden;
    background: var(--bg);
    font-family: "Lato", sans-serif;
  }
  .canvas {
    position: relative;
    width: 1200px;
    height: 1006px;
  }
  .panel {
    position: absolute;
    background: var(--panel);
    border: 2px solid var(--panel-edge);
    border-radius: 18px;
    box-sizing: border-box;
  }
  .door-panel { left: 50px; top: 290px; width: 200px; height: 420px; }
  .side-panel { left: 270px; top: 250px; width: 470px; height: 510px; padding: 36px 30px; }
  .rear-panel { left: 760px; top: 250px; width: 390px; height: 510px; border-radius: 40px 40px 18px 18px; }

  .fairy-illustration {
    position: absolute;
    left: 30px; top: 150px;
    width: 110px; height: 110px;
    border-radius: 50%;
    background: var(--fairy-tone);
  }

  .practice-name {
    margin: 0 0 26px;
    font-size: 38px;
    font-weight: 700;
    color: var(--green);
    letter-spacing: 0.5px;
  }
  .doctor {
    margin: 0;
    font-size: 22px;
    color: var(--grey);
    line-height: 1.45;
  }
  .contact-list {
    list-style: none;
    margin: 30px 0 0;
    padding: 0;
  }
  .contact-item {
    display: flex;
    align-items: center;
    gap: 14px;
    font-size: 19px;
    color: var(--grey);
    padding: 7px 0;
    border-bottom: 1px solid #ececec;
  }
  .contact-item svg { width: 26px; height: 22px; flex: none; }
  .contact-item.email { color: var(--green); }
  .address {
    margin: 22px 0 0;
    font-size: 19px;
    color: var(--grey);
  }
  .website {
    margin: 12px 0 0;
    font-size: 21px;
    color: var(--green);
  }

  .rear-brand {
    position: absolute;
    left: 0; right: 0; top: 120px;
    display: flex;
    flex-direction: column;
    align-items: center;
    gap: 14px;
  }
  .brand-dot {
    width: 90px; height: 90px;
    border-radius: 50%;
    background: var(--green);
  }
  .brand-name {
    font-size: 30px;
    font-weight: 700;
    color: var(--green);
  }
  .rear-website {
    position: absolute;
    left: 0; right: 0; top: 300px;
    text-align: center;
    font-size: 24px;
    font-weight: 700;
    color: var(--green);
  }
  .rear-handle {
    position: absolute;
    left: 165px; top: 360px;
    width: 40px; height: 12px;
    border-radius: 4px;
    background: var(--grey-dark);
  }
</style>
</head>
<body>
<main class="canvas">
  <section class="panel door-panel">
    <div class="fairy-illustration" role="img" aria-label="Illustration: Zahnfee als lachender Zahn mit grünen Flügeln und Zauberstab"></div>
  </section>

  <section class="panel side-panel">
    <h1 class="practice-name">KLARBISS ZAHNÄRZTE</h1>
    <p class="doctor">Dr. med dent. Wolfram Seibel</p>
    <p class="doctor">Dr. med dent. Bernhard Ostrau</p>
    <ul class="contact-list">
      <li class="contact-item">
        <svg viewBox="0 0 26 22" fill="none" stroke="#6e6f70" stroke-width="1.6"><path d="M6 2 L10 7 L8 10 Q11 15 15 17 L18 14 L23 18 L20 21 Q10 20 4 10 Q3 5 6 2 Z"/></svg>
        Telefon: (06831) 98 71 20
      </li>
      <li class="contact-item">
        <svg viewBox="0 0 26 22" fill="none" stroke="#6e6f70" stroke-width="1.6"><rect x="2" y="8" width="22" height="11" rx="2"/><rect x="7" y="2" width="12" height="7"/><line x1="7" y1="14" x2="19" y2="14"/></svg>
        Telefax: (06831) 98 71 22
      </li>
      <li class="contact-item email">
        <svg viewBox="0 0 26 22" fill="none" stroke="#6e6f70" stroke-width="1.6"><rect x="2" y="5" width="22" height="14" rx="1"/><path d="M2 5 L13 13 L24 5"/></svg>
        E-Mail:&nbsp; praxis@zahn-klarbiss.de
      </li>
    </ul>
    <p class="address">Lindenhof-Str. 14, 66740 Saarlouis</p>
    <p class="website">www.zahn-klarbiss.de</p>
  </section>

  <section class="panel rear-panel">
    <div class="rear-brand">
      <span class="brand-dot"></span>
      <span class="brand-name">KLARBISS</span>
    </div>
    <p class="rear-website">www.zahn-klarbiss.de</p>
    <span class="rear-handle"></span>
  </section>
</main>
</body>
</html>
```